Front and back cover design for skincare marketing materials

Thank you for showing an interest in my project.
Project Details.

I require a front and back cover for our marketing materials.
·       Front Cover size: 105 mm W x 150 mm H.
·       Back Cover size:  105 mm W x 150 mm H.
·       It must include these two colors. You can use a third color if you wish.
1.     #DBA09D
2.     #FFFFFF
 
Front Cover
·      The front cover will have a faded image of the Kakadu Plum branch and fruit. There are two image files, KP_image-1.jpg and kp_image-2.jpeg. You can use both images, just a portion of them, or source alternative royalty-free images of Kakadu Plum that may better fit the design. These two files have been uploaded.
 
The front cover wording.
Top of the front cover.
a.     The title of the image. “Kakadu Plum”
b.     The brand name, “Velora Skincare”. The file brand_name.ai uploaded.
 
Bottom of the front cover- Designer's choice of font.
The bottom of the front cover contains three lines of text in the following order.  
1.     Australian Native Ingredients
2.     100% Natural · Organic · Wild-harvested
3.     Australian-Made Premium Skincare
 
Back Cover
·      Back Cover wording.The back cover contains the following words "grown by nature" in white (#FFFFFF) of font Italianno (font_file.ttf) with a background color of #DBA09D as seen in the sample box (sample_box.pdf) right-side panel
 
Please provide one file for the front cover and a separate file for the back cover.
All the elements of the files must be editable.
 
Do NOT use the Curve function on the files, as the text must remain editable/changeable.
 
All assets/resources/files, including fonts not supplied by us but used by the designer, must be named and provided with the finished design.
Updates

Slow to provide project details.

Target Market(s)

Beauty-minded Asian consumers between the ages of 32 and 75 who take a proactive approach to maintaining younger-looking skin. Those who already know the danger of skin damage caused by skincare containing harsh chemicals choose effective natural/organic solutions to meet their skincare needs. Those who wish a more radiant glow and youthful appearance to their skin. Usually, a two-income middle to high-income bracket couples with a mindset for health and beauty.

Industry/Entity Type

beauty

Font styles to use
Other font styles liked:
• I will provide a font file and a brand name file.

Requirements
Must have
• You must use the two colors provided on the product box. The designer may use a third color.
Nice to have
• some gold colour

```html
<!DOCTYPE html>
<html lang="en">
<head>
<meta charset="UTF-8">
<title>Velora Skincare – Kakadu Plum Cover Layout</title>
<link href="https://fonts.googleapis.com/css2?family=Poppins:wght@400;500&family=Italianno&family=Arimo:wght@700&display=swap" rel="stylesheet">
<style>
  :root {
    --stage: #cfd1b2;
    --paper: #ffffff;
    --brand-pink: #d98dad;
    --logo-pink: #dc9bb6;
    --ink: #111111;
    --label: #000000;
    --fold-line: #f0f0f0;
    --fruit-light: #c8f04a;
    --fruit-deep: #7fc21e;
  }
  * { margin: 0; padding: 0; box-sizing: border-box; }
  html, body { width: 1200px; height: 893px; overflow: hidden; }
  body { background: var(--stage); position: relative; font-family: "Poppins", sans-serif; }

  .layout-number {
    position: absolute; left: 45px; top: 52px;
    font: 700 37px/1 "Arimo", sans-serif; color: var(--label);
  }
  .panel-label {
    position: absolute; font-family: "Arimo", sans-serif; font-weight: 700; color: var(--label);
  }
  .panel-label--top { left: 171px; top: 350px; font-size: 30px; line-height: 38px; }
  .panel-label--front { left: 158px; top: 574px; font-size: 49px; line-height: 64px; }
  .panel-label--back { left: 856px; top: 574px; font-size: 49px; line-height: 64px; }

  .guide-arrows { position: absolute; inset: 0; width: 1200px; height: 893px; }

  .cover-front {
    position: absolute; left: 326px; top: 72px; width: 253px; height: 739px;
    background: var(--paper);
    border-radius: 126px 126px 0 0 / 101px 101px 0 0;
  }
  .fold-line {
    position: absolute; left: 0; right: 0; top: 126px; height: 1px; background: var(--fold-line);
  }
  .brand-name {
    position: absolute; left: 0; right: 0; text-align: center;
    font-family: "Poppins", sans-serif; font-weight: 400; font-size: 26px;
    color: var(--logo-pink); letter-spacing: 0.5px;
  }
  .brand-name--flap { top: 232px; }
  .brand-name--front { top: 470px; }
  .product-title {
    position: absolute; left: 0; right: 0; top: 412px; text-align: center;
    font-size: 30px; font-weight: 400; color: var(--ink);
  }
  .fruit-art {
    position: absolute; left: 86px; top: 553px; width: 79px; height: 86px;
    border-radius: 45% 45% 48% 48%;
    background: radial-gradient(circle at 40% 40%, var(--fruit-light), var(--fruit-deep));
  }
  .claims {
    position: absolute; left: 0; right: 0; top: 656px; text-align: center;
    font-size: 10px; font-weight: 500; line-height: 15px; color: var(--ink);
  }

  .cover-back {
    position: absolute; left: 578px; top: 450px; width: 252px; height: 361px;
    background: var(--brand-pink);
  }
  .tagline {
    position: absolute; left: 50%; top: 50%;
    transform: translate(-50%, -50%) rotate(-90deg);
    font-family: "Italianno", cursive; font-size: 58px; color: var(--paper);
    white-space: nowrap; line-height: 1;
  }
</style>
</head>
<body>
  <div class="layout-number">N0.4</div>

  <div class="panel-label panel-label--top">Top<br>Folding</div>
  <div class="panel-label panel-label--front">Front<br>Side</div>
  <div class="panel-label panel-label--back">Back Side</div>

  <svg class="guide-arrows" viewBox="0 0 1200 893" aria-hidden="true">
    <g fill="none" stroke="#000" stroke-width="4">
      <polyline points="222,346 222,283 282,283"/>
      <polyline points="222,571 222,510 282,510"/>
      <polyline points="931,571 931,510 871,510"/>
    </g>
    <g fill="#000">
      <polygon points="292,283 278,275 278,291"/>
      <polygon points="292,510 278,502 278,518"/>
      <polygon points="861,510 875,502 875,518"/>
    </g>
  </svg>

  <section class="cover-front">
    <div class="fold-line"></div>
    <div class="brand-name brand-name--flap">Velora Skincare</div>
    <h1 class="product-title">Kakadu Plum</h1>
    <div class="brand-name brand-name--front">Velora Skincare</div>
    <div class="fruit-art" role="img" aria-label="Illustration of a whole and halved green Kakadu plum"></div>
    <p class="claims">
      Australian Native Ingredients<br>
      100% Natural · Organic · Wild-harvested<br>
      Australian-Made Premium Skincare
    </p>
  </section>

  <section class="cover-back">
    <p class="tagline">grown by nature</p>
  </section>
</body>
</html>
```